Orvela Back & Limb Business Card

Need a business card using the logo provided. I want brand side of the card to be grey with the logo in the center of the card in white.

On the other side I leave to the designers

Target Market(s)

Personal Injury Attorneys

Industry/Entity Type

Medical

Contact Information for Business Card

Name, CEO. Cell Phone, (MARLOWE, Address, Phone) (Homestead, Address, Phone) (Tallahassee, Address, Phone)

Colors

Designer to choose only greyscale colors for use in the design.

Requirements
Must have
• Logo by itself on one side

```html
<!DOCTYPE html>
<html lang="en">
<head>
<meta charset="utf-8">
<title>Orvela Back &amp; Limb Business Card</title>
<link href="https://fonts.googleapis.com/css2?family=Montserrat:wght@600&family=Poppins:wght@300;400;600&display=swap" rel="stylesheet">
<style>
  :root {
    --backdrop: #1f1f1f;
    --card: #626264;
    --ink-light: #ffffff;
    --ink-dark: #111111;
    --glyph: #626264;
  }
  html, body {
    margin: 0;
    width: 1200px;
    height: 1200px;
    overflow: hidden;
    background: var(--backdrop);
  }
  .card {
    position: absolute;
    left: 251px;
    width: 695px;
    height: 396px;
    background: var(--card);
  }
  .card--front { top: 137px; }
  .card--back { top: 591px; }

  .brand {
    position: absolute;
    text-align: center;
    color: var(--ink-light);
    font-family: "Montserrat", sans-serif;
    font-weight: 600;
    line-height: 1;
  }
  .card--front .brand {
    left: 0; right: 0; top: 201px;
  }
  .card--front .brand-name {
    font-size: 64px;
    letter-spacing: 10px;
    padding-left: 10px;
  }
  .card--front .brand-tag {
    font-size: 30px;
    letter-spacing: 7px;
    padding-left: 7px;
    margin-top: 14px;
  }
  .card--back .brand {
    left: 35px; width: 300px; top: 163px;
  }
  .card--back .brand-name {
    font-size: 42px;
    letter-spacing: 6px;
    padding-left: 6px;
  }
  .card--back .brand-tag {
    font-size: 20px;
    letter-spacing: 4.5px;
    padding-left: 4.5px;
    margin-top: 9px;
  }

  .divider {
    position: absolute;
    left: 350px;
    top: 129px;
    width: 1px;
    height: 137px;
    background: var(--ink-light);
  }

  .person {
    position: absolute;
    left: 407px;
    top: 76px;
    font-family: "Poppins", sans-serif;
  }
  .person-name {
    color: var(--ink-light);
    font-weight: 300;
    font-size: 36px;
    letter-spacing: 5px;
    line-height: 1;
  }
  .person-role {
    color: var(--ink-dark);
    font-weight: 600;
    font-size: 19px;
    line-height: 1;
    margin-top: 5px;
  }

  .contacts {
    position: absolute;
    left: 403px;
    top: 170px;
    margin: 0;
    padding: 0;
    list-style: none;
    font-family: "Poppins", sans-serif;
    font-size: 15.5px;
    color: var(--ink-light);
  }
  .contacts li {
    display: flex;
    align-items: center;
    height: 24px;
    margin-bottom: 16.5px;
  }
  .contacts svg {
    width: 21px;
    height: 21px;
    margin-right: 12px;
    flex: none;
  }
</style>
</head>
<body>
  <section class="card card--front">
    <div class="brand">
      <div class="brand-name">ORVELA</div>
      <div class="brand-tag">BACK &amp; LIMB</div>
    </div>
  </section>

  <section class="card card--back">
    <div class="brand">
      <div class="brand-name">ORVELA</div>
      <div class="brand-tag">BACK &amp; LIMB</div>
    </div>

    <div class="divider"></div>

    <div class="person">
      <div class="person-name">MARLOWE</div>
      <div class="person-role">CEO</div>
    </div>

    <ul class="contacts">
      <li>
        <svg viewBox="0 0 20 20" aria-hidden="true">
          <circle cx="10" cy="10" r="10" fill="var(--ink-light)"/>
          <path d="M5 10 L10 5.5 L15 10 M6.5 9 V14.5 H13.5 V9" fill="none" stroke="var(--glyph)" stroke-width="1.6" stroke-linejoin="round"/>
        </svg>
        Street Address Here
      </li>
      <li>
        <svg viewBox="0 0 20 20" aria-hidden="true">
          <circle cx="10" cy="10" r="10" fill="var(--ink-light)"/>
          <rect x="5" y="6.5" width="10" height="7" fill="none" stroke="var(--glyph)" stroke-width="1.3"/>
          <path d="M5 6.5 L10 11 L15 6.5" fill="none" stroke="var(--glyph)" stroke-width="1.3"/>
        </svg>
        hello@orvelaback.com
      </li>
      <li>
        <svg viewBox="0 0 20 20" aria-hidden="true">
          <circle cx="10" cy="10" r="10" fill="var(--ink-light)"/>
          <rect x="5.5" y="8" width="9" height="6" rx="1" fill="var(--glyph)"/>
          <path d="M5 8 Q10 4 15 8" fill="none" stroke="var(--glyph)" stroke-width="1.6"/>
          <circle cx="10" cy="11" r="1.5" fill="var(--ink-light)"/>
        </svg>
        +18 2555 0140 2210
      </li>
      <li>
        <svg viewBox="0 0 20 20" aria-hidden="true">
          <circle cx="10" cy="10" r="10" fill="var(--ink-light)"/>
          <circle cx="10" cy="10" r="5.5" fill="none" stroke="var(--glyph)" stroke-width="1.2"/>
          <ellipse cx="10" cy="10" rx="2.3" ry="5.5" fill="none" stroke="var(--glyph)" stroke-width="1"/>
          <path d="M4.5 10 H15.5" stroke="var(--glyph)" stroke-width="1"/>
        </svg>
        www.orvelaback.com
      </li>
    </ul>
  </section>
</body>
</html>
```